Tendril Harbor

Our product is a subscription-based website for doctors and medical practices. It allows contract-based doctors (locums) to book jobs with medical practices and to organise their own finances (invoicing, pension, etc). Also, it allows medical practices to post jobs, and book locums.

We need a website design that looks clean and professional. It should look easy-to-use and friendly, which will encourage users to sign up as they'll hopefully think using the system will also be simple and friendly.

As well as the homepage, we need a design for the logged-in view. This is very different to the website but equally important. It needs to be very functional. Much more like an application and less like a website.

PLEASE SUBMIT BOTH WEBSITE HOMEPAGE DESIGN AND APPLICATION DASHBOARD DESIGN.

The application is built and we already have a user interface (linked below) so we're not looking for a designer to decide what is on these pages - we already have that. We're ONLY asking for visual design. Please just make the content we have look good. You may move parts of the content around a small amount but the functionality is very much signed off now so it's only visual styling that we need addressed.

Please base the branding around the current logo, which can't be changed. You can get the logo as an EPS here : http://clients.brassowl.co.uk/tendrilharbor/design/logo-green.eps

Here is a link to the current design for the website, and for the application dashboard:
http://clients.brassowl.co.uk/tendrilharbor/design/

Also, here is a video we've had made which might help you with the brand:
http://quivlo.com/71825364
Updates

Just in case it isn't clear, the video (linked in the main brief) is an essential part of the website homepage.

Reason: We need to spend some time looking over these designs and might ask for a few amendments to one or two in the next few days. Thanks.

Target Market(s)

Doctors and medical practices

Industry/Entity Type

Medical

Requirements
Must have
• It must have all the features that are in the linked designs - homepage and dashboard.

```html
<!DOCTYPE html>
<html lang="en">
<head>
<meta charset="utf-8">
<title>Tendril Harbor – A network for connecting locums with employers</title>
<link rel="stylesheet" href="https://fonts.googleapis.com/css2?family=Open+Sans:wght@400;600;700&display=swap">
<style>
:root{
  --blue:#1d8fcf;
  --blue-dark:#0d72b0;
  --blue-deep:#1571a8;
  --green:#5b9a1b;
  --green-dark:#4a7f12;
  --ink:#3b3b3b;
  --muted:#5a5a5a;
  --line:#cfcfcf;
  --header-bg:#efefef;
  --white:#ffffff;
}
*{box-sizing:border-box;margin:0;padding:0}
html,body{width:732px;height:1200px;overflow:hidden;background:var(--white)}
body{font-family:"Open Sans",Arial,sans-serif;color:var(--ink)}
.page{position:relative;width:732px;height:1200px;overflow:hidden}
.abs{position:absolute}

/* header */
.site-header{left:0;top:0;width:732px;height:100px;background:var(--header-bg);border-bottom:1px solid #d8d8d8}
.brand{left:92px;top:14px;display:flex;align-items:center;gap:10px}
.brand-mark{width:60px;height:60px;border-radius:50%;background:var(--blue-deep)}
.brand-name{font-size:26px;font-weight:700;color:var(--blue-deep);line-height:1;letter-spacing:.5px}
.brand-tagline{left:173px;top:64px;font-size:10px;color:var(--blue-deep)}
.user-name{right:82px;top:20px;font-size:11px;font-weight:700;color:var(--green)}
.user-actions{right:78px;top:39px;display:flex;align-items:center;gap:8px;font-size:10px;color:var(--muted)}
.btn-dashboard{background:var(--blue);color:#fff;font-weight:600;padding:3px 10px;border-radius:6px}

/* nav */
.main-nav{left:75px;top:100px;width:584px;height:32px;background:linear-gradient(var(--blue),var(--blue-dark));border-radius:0 0 4px 4px;display:flex;justify-content:center;align-items:center;gap:10px;font-size:10.5px;font-weight:600;color:#fff}
.main-nav .sep{opacity:.8}
.main-nav .current{background:#fff;color:var(--blue-dark);padding:1px 8px;border-radius:3px}

/* hero */
.video{left:100px;top:148px;width:240px;height:166px;background:#111}
.video-frame{width:240px;height:138px;background:linear-gradient(135deg,#d9dde0,#b9c4cb 55%,#8a9aa4)}
.video-play{left:102px;top:64px;width:54px;height:54px;background:rgba(100,170,30,.85);border-radius:6px}
.video-controls{left:10px;top:144px;width:220px;height:16px}
.hero-title{left:354px;top:146px;font-size:18.5px;line-height:22px;color:var(--ink)}
.hero-title strong{color:var(--green);font-weight:600}
.hero-list{left:354px;top:207px;list-style:none;font-size:12px;line-height:18px;color:var(--ink)}
.hero-list li::before{content:"⊕";color:var(--green);font-size:10px;margin-right:3px}
.hero-object{left:492px;top:190px;width:150px;height:130px;border-radius:50%/45%;background:radial-gradient(circle at 45% 60%,#e8eef2,#9fc6de 55%,#ffffff 75%)}
.btn-hero{left:348px;top:289px;width:165px;height:26px;background:linear-gradient(#6aa828,var(--green-dark));color:#fff;font-size:11px;font-weight:600;border-radius:5px;display:flex;align-items:center;justify-content:center}
.hero-divider{left:40px;top:332px;width:652px;height:6px;background:radial-gradient(ellipse at center,rgba(0,0,0,.18),rgba(0,0,0,0) 70%)}

/* audience columns */
.audience{width:262px}
.audience h2{font-size:14px;font-weight:700;padding-bottom:4px;border-bottom:1px solid var(--line)}
.audience .lead{font-size:10.5px;margin:10px 0 6px}
.audience h3{font-size:11px;font-weight:700;margin-top:6px}
.audience p{font-size:8.8px;line-height:11.5px;color:var(--muted);padding-left:15px;margin-top:3px}
.audience--locum{left:93px;top:366px}
.audience--locum h2,.audience--locum .lead{color:var(--blue)}
.audience--employer{left:384px;top:366px}
.audience--employer h2,.audience--employer .lead{color:var(--green)}
.audience-cta{display:flex;gap:12px;margin-top:12px}
.audience-cta .field{width:190px;height:20px;border:1px solid #c9c9c9;border-radius:3px;font-size:8.5px;color:#9a9a9a;padding:4px 6px;white-space:nowrap;overflow:hidden}
.audience-cta .btn{width:62px;height:20px;border-radius:2px;color:#fff;font-size:9.5px;display:flex;align-items:center;justify-content:center}
.audience--locum .btn{background:var(--blue)}
.audience--employer .btn{background:var(--green)}
.column-frame{top:590px;width:288px;height:12px;border:1px solid #ddd;border-top:none;border-radius:0 0 8px 8px}

/* steps bar */
.steps{left:78px;top:610px;width:581px;height:28px;background:linear-gradient(var(--blue),var(--blue-dark));border-radius:3px;display:flex;align-items:center;justify-content:space-around;color:#fff;font-size:10.5px}
.steps span b{display:inline-flex;width:15px;height:15px;border-radius:50%;background:#fff;color:var(--blue);font-size:9px;align-items:center;justify-content:center;margin-right:6px}

/* signup */
.signup{left:75px;top:641px;width:584px;height:203px;border:1px solid #d6d6d6;border-top:none;border-radius:0 0 8px 8px;overflow:hidden}
.signup h2{position:absolute;left:11px;top:15px;font-size:13.5px;font-weight:400;color:var(--ink)}
.signup .role{position:absolute;left:11px;top:48px;font-size:9.5px;display:flex;gap:12px;align-items:center}
.radio{display:inline-block;width:10px;height:10px;border:2px solid var(--blue);border-radius:50%;vertical-align:-1px;margin-right:2px}
.signup label{position:absolute;font-size:10px}
.signup .input{position:absolute;width:135px;height:22px;border:1px solid #c4c4c4;border-radius:4px}
.signup .terms{position:absolute;left:11px;top:162px;font-size:10.5px;display:flex;align-items:center;gap:5px}
.check{width:9px;height:9px;border:2px solid var(--blue);background:linear-gradient(var(--blue),var(--blue)) center/3px 3px no-repeat}
.signup-photo{position:absolute;left:360px;top:68px;width:224px;height:135px;background:linear-gradient(160deg,#f5ece4,#cfe6f1 45%,#5fb7dd)}

/* press */
.press{top:863px;width:180px;height:130px;border:1px solid #cfcfcf;border-radius:4px;overflow:hidden}
.press-name{height:38px;border-bottom:1px solid #cfcfcf;box-shadow:0 2px 3px rgba(0,0,0,.08);display:flex;align-items:center;justify-content:center;font-size:17px;font-weight:700;color:#1a2a44}
.press-quote{position:relative;padding:20px 24px 0 28px;font-size:9px;line-height:14px;color:var(--muted)}
.press-quote::before,.press-quote::after{position:absolute;font-size:40px;color:#c9e2f1;font-family:Georgia,serif;line-height:1}
.press-quote::before{content:"\201C";left:14px;top:6px}
.press-quote::after{content:"\201D";right:14px;top:40px}

/* footer */
.testimonials{left:0;top:1007px;width:732px;height:90px;background:var(--blue);border-top:3px solid var(--green);color:#fff;font-size:10.5px;font-weight:600;line-height:13px;text-align:center}
.testimonials blockquote{position:absolute;top:24px;width:232px}
.footer-nav{left:0;top:1097px;width:732px;height:33px;background:var(--green);display:flex;justify-content:center;align-items:center;gap:13px;color:#fff;font-size:10.5px;font-weight:600}
.footer-info{left:0;top:1130px;width:732px;height:55px;background:var(--blue);color:#fff;text-align:center;font-size:10.5px;font-weight:600;line-height:14px;padding-top:7px}
.footer-info .help{margin-bottom:4px}
.legal{left:0;top:1187px;width:732px;text-align:center;font-size:6.8px;color:#444}
.legal span{margin:0 10px}
</style>
</head>
<body>
<div class="page">

  <header class="site-header abs">
    <div class="brand abs">
      <span class="brand-mark"></span>
      <span class="brand-name">TENDRIL HARBOR</span>
    </div>
    <div class="brand-tagline abs">Get Connected. Stay organised.</div>
    <div class="user-name abs">Mrs. Rosalind Vetch</div>
    <div class="user-actions abs"><span>Sign out</span><span class="btn-dashboard">Go to Dashboard</span></div>
  </header>

  <nav class="main-nav abs">
    <span class="current">Home</span><span class="sep">|</span>
    <span>Locums</span><span class="sep">|</span>
    <span>Employers</span><span class="sep">|</span>
    <span>Pricing</span><span class="sep">|</span>
    <span>About us</span><span class="sep">|</span>
    <span>FAQ</span><span class="sep">|</span>
    <span>Contact us</span>
  </nav>

  <section class="video abs">
    <div class="video-frame" role="img" aria-label="Video still: doctors talking around a laptop"></div>
    <div class="video-play abs">
      <svg width="54" height="54" viewBox="0 0 54 54"><path d="M20 15 L40 27 L20 39 Z" fill="#fff" opacity=".9"/></svg>
    </div>
    <svg class="video-controls abs" viewBox="0 0 220 16" width="220" height="16">
      <rect x="8" y="2" width="14" height="12" rx="1" fill="#5b9a1b"/>
      <path d="M12 5 L19 8 L12 11 Z" fill="#fff"/>
      <rect x="30" y="6" width="140" height="4" rx="2" fill="#ddd"/>
      <rect x="30" y="6" width="48" height="4" rx="2" fill="#777"/>
      <rect x="52" y="3" width="3" height="10" fill="#6aa828"/>
      <rect x="184" y="10" width="3" height="3" fill="#6aa828"/>
      <rect x="189" y="8" width="3" height="5" fill="#6aa828"/>
      <rect x="194" y="6" width="3" height="7" fill="#6aa828"/>
      <rect x="199" y="3" width="3" height="10" fill="#888"/>
      <path d="M208 4 h3 M208 4 v3 M217 4 h-3 M217 4 v3 M208 12 h3 M208 12 v-3 M217 12 h-3 M217 12 v-3" stroke="#ccc" stroke-width="1"/>
    </svg>
  </section>

  <h1 class="hero-title abs" style="font-weight:400">A Network for connecting<br><strong>Locums</strong> with employers</h1>
  <ul class="hero-list abs">
    <li>Better connectivity</li>
    <li>More choice</li>
    <li>Less paperwork</li>
    <li>Lower costs</li>
  </ul>
  <div class="hero-object abs" role="img" aria-label="Illustration of a stethoscope"></div>
  <div class="btn-hero abs">Sign up for free-try us out</div>
  <div class="hero-divider abs"></div>

  <section class="audience audience--locum abs">
    <h2>GP Locums</h2>
    <p class="lead" style="padding:0;color:var(--blue);font-size:10.5px">The complete platform to organise your locum life</p>
    <h3>① Find Jobs</h3>
    <p>Search, apply and get invited for a wide selection of jobs from practices and agencies</p>
    <h3>② Do your locum admin easily online</h3>
    <p>Profile, diary management, invoicing, pension forms, finances, tax returns</p>
    <h3>③ Create and grow your “Employer Network”</h3>
    <p>Create your online profile and connect with your own network of employers allowing you to automatically fill jobs</p>
    <div class="audience-cta"><span class="field">More about Tendril Harbor for locums</span><span class="btn">Sign Up</span></div>
  </section>
  <div class="column-frame abs" style="left:78px"></div>

  <section class="audience audience--employer abs">
    <h2>Employers</h2>
    <p class="lead" style="padding:0;color:var(--green);font-size:10.5px">The complete platform to organise your locum life</p>
    <h3>① Find locums</h3>
    <p>Post your locumm requirements. Search and employ the right locums via your e-book system</p>
    <h3>② Do your locum admin easily online</h3>
    <p>Profile, diary management, pre-employment checks, locum market statistics</p>
    <h3>③ Create and grow your “employer network”</h3>
    <p>Create your online profile and connect with your own network of locums allowing them to automatically fill jobs</p>
    <div class="audience-cta"><span class="field">More about Tendril Harbor for employers</span><span class="btn">Sign Up</span></div>
  </section>
  <div class="column-frame abs" style="left:368px"></div>

  <div class="steps abs">
    <span><b>1</b>"The network" for Locums and employers</span>
    <span><b>2</b>Save time and Cost</span>
    <span><b>3</b>Try it free now</span>
  </div>

  <section class="signup abs">
    <h2>Try it now with just an email address, GMC number and password!</h2>
    <div class="role"><span>I am</span><span><i class="radio"></i>a Locum</span><span><i class="radio"></i>an employer</span></div>
    <label style="left:11px;top:74px">Email</label>
    <span class="input" style="left:10px;top:90px"></span>
    <label style="left:168px;top:74px">GMC number</label>
    <span class="input" style="left:168px;top:90px"></span>
    <label style="left:11px;top:115px">Password:</label>
    <span class="input" style="left:10px;top:130px"></span>
    <label style="left:170px;top:115px">Confirm password:</label>
    <span class="input" style="left:168px;top:130px"></span>
    <div class="terms"><span class="check"></span>I agree to the terms of service and the privacy policy</div>
    <div class="signup-photo" role="img" aria-label="Photo of a smiling nurse holding a clipboard"></div>
  </section>

  <article class="press abs" style="left:78px">
    <div class="press-name">morningledger.co.uk</div>
    <p class="press-quote">Lorem ipsum dolor sit amet, consectetur adipiscing elit. Cras justo elit, ultrices viverra adipiscing ut.</p>
  </article>
  <article class="press abs" style="left:277px">
    <div class="press-name">Courier Online</div>
    <p class="press-quote">Lorem ipsum dolor sit amet, consectetur adipiscing elit. Cras justo elit, ultrices viverra adipiscing ut.</p>
  </article>
  <article class="press abs" style="left:477px">
    <div class="press-name">The Lantern</div>
    <p class="press-quote">Lorem ipsum dolor sit amet, consectetur adipiscing elit. Cras justo elit, ultrices viverra adipiscing ut.</p>
  </article>

  <section class="testimonials abs">
    <blockquote style="left:68px">So easy to set up.Five minutes and you’re in.And it does all the boring admin stuff that i hate.<br>Name of person,Locum</blockquote>
    <blockquote style="left:434px">As a Practise, it’s great to be able to find Locums quickly and easily.No more time-consuming agency phone calls!<br>Blah Medical Centre</blockquote>
  </section>

  <nav class="footer-nav abs">
    <span>Home</span><span>Locums</span><span>Employers</span><span>About us</span><span>FAQ</span><span>Contact us</span>
  </nav>

  <footer class="footer-info abs">
    <div class="help">We’re here to help : support@tendrilharbor.co.uk</div>
    <div>Copyright © 2013 Tendril Harbor Ltd. All Rights Reserved</div>
    <div>Registered in England no.08815327</div>
  </footer>

  <div class="legal abs"><span>Terms of service</span>|<span>Privacy policy</span>|<span>Refund policy</span></div>

</div>
</body>
</html>
```